Business Card for my building company

I would like the card to make a statement, so as soon as you see the card you think "wow nice card' and then read the details on the card its self. Also i would like to be able to put in the detail for the MUST HAVES so please Crete a box that i can alter depending on who in my business needs the cards. Thank you

Target Market(s)

Any one looking to build a house/ townhouse or duplex

Industry/Entity Type

Home Builder

Contact Information for Business Card

I would like the card to have the logo on the card and the must haves

Font styles to use
Sans Serif

Requirements
Must have
• Name
• Phone Number
• Email Address
• Website
• Licence Number
• Abn

```html
<!DOCTYPE html>
<html lang="en">
<head>
<meta charset="utf-8">
<title>Corelan Builders – Business Card</title>
<link href="https://fonts.googleapis.com/css2?family=Arimo:wght@400;700&display=swap" rel="stylesheet">
<style>
  :root {
    --gold: #c9a14c;
    --gold-light: #d9b866;
    --gold-dark: #b08634;
    --white: #ffffff;
    --ink: #161616;
    --stage: #ece8e1;
  }
  * { margin: 0; padding: 0; box-sizing: border-box; }
  html, body {
    width: 1200px; height: 950px; overflow: hidden;
    background: var(--stage);
    font-family: "Arimo", Arial, sans-serif;
  }
  .sheet {
    width: 1200px; height: 950px;
    display: flex; flex-direction: column;
    align-items: center; justify-content: center; gap: 40px;
  }
  .card {
    width: 760px; height: 430px;
    position: relative; overflow: hidden;
    box-shadow: 0 12px 30px rgba(0,0,0,0.25);
  }

  /* Brand lockup: name in one colour and weight, one plain square beside it */
  .brand {
    display: flex; align-items: center; gap: 16px;
    font-weight: 700; color: var(--ink);
    text-transform: uppercase; letter-spacing: 2px;
  }
  .brand-mark { display: block; background: var(--ink); }

  /* Front */
  .card-front {
    background: linear-gradient(135deg, var(--gold-light), var(--gold) 55%, var(--gold-dark));
    display: flex; flex-direction: column; align-items: center; justify-content: center;
  }
  .card-front .brand { font-size: 46px; }
  .card-front .brand-mark { width: 58px; height: 58px; }
  .card-front .web {
    margin-top: 40px; color: var(--white);
    font-size: 17px; letter-spacing: 7px;
  }

  /* Back */
  .card-back { background: var(--white); }
  .card-back .upper {
    height: 262px; padding-top: 10px;
    display: flex; flex-direction: column; align-items: center; justify-content: center;
  }
  .card-back .brand { font-size: 40px; }
  .card-back .brand-mark { width: 50px; height: 50px; }
  .person-name {
    margin-top: 28px; color: var(--gold);
    font-size: 24px;
  }
  .divider {
    height: 7px; background: var(--ink);
    box-shadow: 0 2px 4px rgba(0,0,0,0.35);
    position: relative; z-index: 1;
  }
  .details {
    position: absolute; left: 0; right: 0; bottom: 0; top: 269px;
    background: linear-gradient(135deg, var(--gold-light), var(--gold) 60%, var(--gold-dark));
    color: var(--white);
    display: flex; flex-direction: column; align-items: center; justify-content: center;
    gap: 10px; font-size: 18px;
  }
  .detail-row { display: flex; align-items: center; gap: 24px; }
  .detail-item { display: flex; align-items: center; gap: 8px; }
  .icon { width: 18px; height: 18px; fill: var(--white); }
</style>
</head>
<body>
<main class="sheet">
  <section class="card card-front">
    <div class="brand"><span class="brand-mark"></span>Corelan Builders</div>
    <p class="web">www.corelanbuild.com</p>
  </section>

  <section class="card card-back">
    <div class="upper">
      <div class="brand"><span class="brand-mark"></span>Corelan Builders</div>
      <p class="person-name">Sam Hartley</p>
    </div>
    <div class="divider"></div>
    <div class="details">
      <div class="detail-row">
        <span class="detail-item">Abn 7654321</span>
        <span class="detail-item">Licence No. 204816</span>
      </div>
      <div class="detail-row">
        <span class="detail-item">
          <svg class="icon" viewBox="0 0 24 24" aria-hidden="true"><path d="M6.6 10.8a15.1 15.1 0 0 0 6.6 6.6l2.2-2.2a1 1 0 0 1 1-.25 11.4 11.4 0 0 0 3.6.57 1 1 0 0 1 1 1V20a1 1 0 0 1-1 1A17 17 0 0 1 3 4a1 1 0 0 1 1-1h3.5a1 1 0 0 1 1 1c0 1.25.2 2.45.57 3.57a1 1 0 0 1-.25 1z"/></svg>
          555 0142 7788
        </span>
        <span class="detail-item">
          <svg class="icon" viewBox="0 0 24 24" aria-hidden="true"><path d="M2 5h20v14H2z M3.5 6.5 12 13l8.5-6.5" fill="none" stroke="#fff" stroke-width="2"/></svg>
          name@corelanbuild.com
        </span>
      </div>
      <div class="detail-row">
        <span class="detail-item">
          <svg class="icon" viewBox="0 0 24 24" aria-hidden="true"><circle cx="12" cy="12" r="9.5" fill="none" stroke="#fff" stroke-width="2"/><path d="M2.5 12h19M12 2.5c3 3 3 16 0 19M12 2.5c-3 3-3 16 0 19" fill="none" stroke="#fff" stroke-width="1.6"/></svg>
          www.corelanbuild.com
        </span>
      </div>
    </div>
  </section>
</main>
</body>
</html>
```